business cards

we want our logos on the back
the information on it are on the design I've uploaded
come up with whatever you think is best, we want something professional, sophisticated and sleek.

```html
<!DOCTYPE html>
<html lang="en">
<head>
<meta charset="utf-8">
<title>Crest Health and Performance — Business Cards</title>
<link rel="stylesheet" href="https://fonts.googleapis.com/css2?family=Lato:wght@400;700&display=swap">
<style>
  :root {
    --backdrop: #2a2a2a;
    --card-dark: #1c1c1c;
    --card-light: #ffffff;
    --brand-green: #4cb848;
    --ink-light: #ffffff;
    --ink-dark: #1c1c1c;
  }
  * { margin: 0; padding: 0; box-sizing: border-box; }
  html, body {
    width: 1200px; height: 895px; overflow: hidden;
    background: var(--backdrop);
    font-family: "Lato", sans-serif;
  }
  .card-pair {
    position: absolute; left: 261px; top: 173px;
    display: flex; gap: 51px;
  }
  .card {
    position: relative; width: 314px; height: 549px;
    border-radius: 13px; overflow: hidden;
    box-shadow: 0 6px 18px rgba(0,0,0,.35);
  }
  /* Front */
  .card--front { background: var(--card-light); }
  .front-lower {
    position: absolute; left: 0; right: 0; top: 236px; bottom: 0;
    background: var(--card-dark);
    border-top: 5px solid var(--brand-green);
  }
  .front-brand {
    position: absolute; left: 34px; top: 96px;
    display: flex; align-items: center; gap: 12px;
  }
  .front-brand__dot {
    width: 11px; height: 11px; border-radius: 50%;
    background: var(--brand-green);
  }
  .front-brand__name {
    font-weight: 400; font-size: 30px; letter-spacing: .3em;
    color: var(--ink-dark);
  }
  .holder {
    position: absolute; right: 37px; top: 296px;
    text-align: right; color: var(--ink-light);
  }
  .holder__name {
    font-weight: 700; font-size: 24px; color: var(--brand-green);
    letter-spacing: .02em; line-height: 28px;
  }
  .holder__role { font-size: 15px; line-height: 18.5px; letter-spacing: .02em; }
  .contact-list {
    position: absolute; right: 37px; top: 425px;
    list-style: none; color: var(--ink-light);
  }
  .contact-list li {
    display: flex; justify-content: flex-end; align-items: center;
    gap: 10px; font-size: 15.5px; height: 19.5px;
    letter-spacing: .02em;
  }
  .contact-list li:last-child { margin-top: 2px; }
  .contact-list svg { width: 13px; height: 13px; fill: var(--brand-green); flex: none; }
  /* Back */
  .card--back { background: var(--card-dark); text-align: center; color: var(--ink-light); }
  .back-brand { position: absolute; left: 0; right: 0; top: 359px; }
  .back-brand__name {
    font-weight: 400; font-size: 42px; letter-spacing: .45em;
    margin-left: .45em; line-height: 46px;
  }
  .back-brand__sub {
    font-weight: 400; font-size: 9px; letter-spacing: .55em;
    margin-left: .55em; line-height: 12px;
  }
  .services {
    position: absolute; left: 0; right: 0; top: 449px;
    color: var(--brand-green); font-size: 14px; letter-spacing: .1em;
    line-height: 19.5px;
  }
</style>
</head>
<body>
  <main class="card-pair">
    <section class="card card--front" aria-label="Card front">
      <div class="front-lower"></div>
      <div class="front-brand">
        <span class="front-brand__name">CREST</span>
        <span class="front-brand__dot"></span>
      </div>
      <div class="holder">
        <h1 class="holder__name">MARCUS DELANEY</h1>
        <p class="holder__role">Director-</p>
        <p class="holder__role">Personal Trainer</p>
        <p class="holder__role">Sport Nutritionist</p>
        <p class="holder__role">BExSc</p>
      </div>
      <ul class="contact-list">
        <li>03 9000 1482
          <svg viewBox="0 0 24 24"><path d="M6.6 10.8a15 15 0 0 0 6.6 6.6l2.2-2.2c.3-.3.7-.4 1-.2 1.1.4 2.3.6 3.6.6.6 0 1 .4 1 1V20c0 .6-.4 1-1 1A17 17 0 0 1 3 4c0-.6.4-1 1-1h3.5c.6 0 1 .4 1 1 0 1.3.2 2.5.6 3.6.1.3 0 .7-.2 1z"/></svg>
        </li>
        <li>03 9000 1497
          <svg viewBox="0 0 24 24"><path d="M6 2h12v5H6zM4 8h16a2 2 0 0 1 2 2v7h-4v5H6v-5H2v-7a2 2 0 0 1 2-2zm4 7v5h8v-5z"/></svg>
        </li>
        <li>hello@crestfitco.com.au
          <svg viewBox="0 0 24 24"><path d="M2 5h20v2l-10 6L2 7zm0 4 10 6 10-6v10H2z"/></svg>
        </li>
        <li>12 Linden Rd, Northvale
          <svg viewBox="0 0 24 24"><path d="M12 1a8 8 0 0 0-8 8c0 6 8 14 8 14s8-8 8-14a8 8 0 0 0-8-8zm0 11a3 3 0 1 1 0-6 3 3 0 0 1 0 6z"/></svg>
        </li>
      </ul>
    </section>

    <section class="card card--back" aria-label="Card back">
      <div class="back-brand">
        <p class="back-brand__name">CREST</p>
        <p class="back-brand__sub">HEALTH AND PERFORMANCE</p>
      </div>
      <div class="services">
        <p>PHYSIO &nbsp;|&nbsp; S&amp;C &nbsp;|&nbsp; COACHING</p>
        <p>PERSONAL TRAINING</p>
        <p>REHAB &nbsp;|&nbsp; RECOVERY</p>
      </div>
    </section>
  </main>
</body>
</html>
```